High end boutique food product label

We are looking for a label design to be used on our range of high end food products. We don't have a design or colour scheme in mind and are interested to see what ideas are submitted.
We would like it to feel sophisticated, chic, and eye-catching.
All of our products are handmade in Australia using Australian ingredients.
The graphics for the label will need to be scaleable to be fit a variety of labels from small squat jars with labels sized 3.5cm high and 7cm wide, to tall thin bottles with labels that are 14cm high and 4.5cm wide.
We would be interested in working with the winning designer to create these different sized labels.
The label submitted for this project should be 14cm high and 4.5cm wide, it should include our logo (file supplied in .jpeg and .ai), the product name 'Extra Virgin Olive Oil' and the size '250ml'.
This is just the front label on a bottle, we are not expecting a rear label to be created currently.
You are welcome to use any fonts you think will look good but the fonts used in our logo are Allaina Medium and Bebas Kai Regular.

```html
<!DOCTYPE html>
<html lang="en">
<head>
<meta charset="utf-8">
<title>Calder &amp; Wren Provisions – Extra Virgin Olive Oil Label</title>
<link href="https://fonts.googleapis.com/css2?family=Alice&family=Montserrat:wght@600&display=swap" rel="stylesheet">
<style>
  :root {
    --stage: #1e1e1e;
    --paper: #f2f1ef;
    --brown: #4a2a1a;
    --gold: #b79a64;
    --band-gold: #e4cc98;
    --white: #ffffff;
  }
  html, body {
    margin: 0;
    padding: 0;
    width: 1200px;
    height: 1200px;
    overflow: hidden;
    background: var(--stage);
  }
  .canvas {
    position: relative;
    width: 1200px;
    height: 1200px;
    background: var(--stage);
  }
  .label {
    position: absolute;
    left: 426px;
    top: 60px;
    width: 348px;
    height: 1080px;
    background: var(--paper);
    overflow: hidden;
  }
  .brand {
    position: absolute;
    top: 120px;
    left: 0;
    width: 100%;
    margin: 0;
    text-align: center;
    color: var(--brown);
    font-family: "Alice", Georgia, serif;
    font-weight: 400;
    font-size: 44px;
    line-height: 1.1;
  }
  .brand-line {
    display: block;
  }
  .divider {
    position: absolute;
    top: 290px;
    left: 0;
    width: 100%;
    height: 9px;
    background: var(--band-gold);
  }
  .product-name {
    position: absolute;
    left: 0;
    width: 100%;
    text-align: center;
    margin: 0;
    font-family: "Alice", Georgia, serif;
    font-weight: 400;
    color: var(--brown);
    line-height: 1;
  }
  .product-name.line-1 { top: 326px; font-size: 86px; }
  .product-name.line-2 { top: 412px; font-size: 86px; }
  .product-name.line-3 { top: 622px; font-size: 74px; }
  .sprig {
    position: absolute;
    top: 542px;
    left: 85px;
    width: 178px;
    height: 70px;
    background: linear-gradient(90deg, rgba(74,42,26,0.15), rgba(74,42,26,0.35), rgba(74,42,26,0.15));
    border-radius: 35px;
  }
  .botanical {
    position: absolute;
    top: 766px;
    left: 0;
    width: 100%;
    height: 257px;
    background: linear-gradient(180deg, rgba(183,154,100,0.08), rgba(183,154,100,0.32));
  }
  .volume-band {
    position: absolute;
    bottom: 0;
    left: 0;
    width: 100%;
    height: 57px;
    background: var(--brown);
    color: var(--white);
    font-family: "Montserrat", Arial, sans-serif;
    font-weight: 600;
    font-size: 28px;
    line-height: 57px;
    text-align: center;
  }
</style>
</head>
<body>
  <main class="canvas">
    <section class="label">
      <p class="brand">
        <span class="brand-line">Calder &amp; Wren</span>
        <span class="brand-line">Provisions</span>
      </p>
      <div class="divider"></div>

      <h1 class="product-name line-1">Extra</h1>
      <h1 class="product-name line-2">Virgin</h1>
      <div class="sprig" role="img" aria-label="Small dark brown olive sprig ornament"></div>
      <h1 class="product-name line-3">Olive Oil</h1>

      <div class="botanical" role="img" aria-label="Gold line-engraved illustration of olive branches with olives, leaves and blossoms"></div>
      <div class="volume-band">250ml</div>
    </section>
  </main>
</body>
</html>
```